BOND WITH TOBY FOR SPECIALISED ADHESIVE AND SEALANTS.

Details for my new Banner Ad Design Project will be added soon.
All that I am looking for is WORDING that can demonstrate to potential customers what the products can achieve and describing the various materials that this special adhesive will stick and why they need to choose it also a logo or even new name to fit in if financially possible
The size of the banner is unimportant as I only need help in getting the message over then I will adjust accordingly or pay the designer to complete.
As I am very limited in my knowledge of web design in fact it is non existent your help is paramount for the result.
This is a new project for me as I am now a young retired person who is looking for something different to follow.
Please let me know if the information I supply is in sufficient,
Best regards to all and in your design careers.
Updates

As pointed out to me that my request is to broad for a result,but I am not looking for words that describe a space shot, I am looking for suggestions to help me to put together some form of ad that helps me get the business off the ground ,I am no expert in marketing and design, so any format of words would be helpful,thank you all and remember, " you are the experts".

Target Market(s)

General public in the UK,and commercial business.
It would be used where there is a requirement to seal/or stick difficult materials or items but not large items like roofs/buildings etc.

Industry/Entity Type

Adhesive

Font styles to use
Sans Serif

Colors

Designer to choose colors to be used in the design.

Requirements
Must have
• To make people feel they will need the product or service maybe not initially but soon.
Nice to have
• This can be anything related to sticking or sealing different household products,
Should not have
• old fashioned font

```html
<!DOCTYPE html>
<html lang="en">
<head>
<meta charset="utf-8">
<title>Bond with Toby – Banner</title>
<link rel="stylesheet" href="https://fonts.googleapis.com/css2?family=Yesteryear&family=Josefin+Sans:wght@400;600&display=swap">
<style>
  :root {
    --page-bg: #e5e5e5;
    --banner-bg: #ffffff;
    --plum: #5a3340;
    --teal: #2e9a94;
    --skin: #f3dcc4;
    --button-text: #ffffff;
  }
  html, body {
    margin: 0;
    padding: 0;
    width: 1200px;
    height: 900px;
    overflow: hidden;
    background: var(--page-bg);
  }
  .banner {
    position: absolute;
    left: 198px;
    top: 342px;
    width: 805px;
    height: 214px;
    background: var(--banner-bg);
    border-radius: 2px;
  }
  .mascot {
    position: absolute;
    left: 30px;
    top: 20px;
    width: 140px;
    height: 186px;
    border-radius: 8px;
    background: linear-gradient(180deg, var(--skin) 0%, var(--teal) 45%, var(--plum) 100%);
  }
  .headline {
    position: absolute;
    left: 166px;
    top: 8px;
    width: 610px;
    margin: 0;
    text-align: center;
    font-family: "Yesteryear", cursive;
    font-weight: 400;
    font-size: 96px;
    line-height: 1.1;
    color: var(--plum);
    white-space: nowrap;
  }
  .tagline {
    position: absolute;
    left: 178px;
    top: 124px;
    width: 588px;
    margin: 0;
    text-align: center;
    font-family: "Josefin Sans", sans-serif;
    font-weight: 400;
    font-size: 21px;
    letter-spacing: 1.2px;
    color: var(--plum);
    white-space: nowrap;
  }
  .cta {
    position: absolute;
    left: 384px;
    top: 164px;
    width: 116px;
    height: 33px;
    display: flex;
    align-items: center;
    justify-content: center;
    background: var(--teal);
    color: var(--button-text);
    border-radius: 5px;
    font-family: "Josefin Sans", sans-serif;
    font-weight: 600;
    font-size: 15px;
    letter-spacing: 1.5px;
    text-decoration: none;
    padding-top: 2px;
    box-sizing: border-box;
  }
</style>
</head>
<body>
  <section class="banner">
    <div class="mascot" role="img" aria-label="Cartoon handyman mascot in a teal jumper giving a thumbs up"></div>
    <h1 class="headline">Bond with Toby</h1>
    <p class="tagline">FOR SPECIALISED ADHESIVE AND SEALANTS</p>
    <a class="cta" href="#">CLICK ME</a>
  </section>
</body>
</html>
```